A Student Forum developed (or Plugin tweaked) and installed on our current Wordpress Website

We require a Student Forum with LOGIN from our current Website.

Current website reference : www.harcombelearning.edu.au

The student forum is for students to ask questions about their studies and for ADMINS to reply.

The student forum should be able to cater for development of CATEGORIES. I have included a picture shot of the old forum in Joomla for understanding.

This job includes the overall design and also installation. It is perfectly fine, if the user sources a suitable Plugin as the basis of the forum, tweaks it to our branding and installs.

Please review the general look and feel of the website for branding.

Target Market(s)

Students

Industry/Entity Type

Education

Font styles to use
Sans Serif

Colors
ffffff

Requirements
Must have
• Categories in Forum - levels of administration
Nice to have
• uploads and downloads would be good
• place for student photo
• News etc.

```html
<!DOCTYPE html>
<html lang="en">
<head>
<meta charset="utf-8">
<title>Harcombe Learning – Recent Forum Questions</title>
<link href="https://fonts.googleapis.com/css2?family=Roboto:wght@300;400;500&display=swap" rel="stylesheet">
<style>
:root{
  --navy:#1f3760;
  --navy-dark:#172a4b;
  --badge-navy:#253f69;
  --gold:#d3913f;
  --footer:#d09048;
  --page:#e4e4e4;
  --card:#ffffff;
  --line:#d4d6da;
  --text-nav:#2d3c58;
  --icon:#7182a6;
  --meta:#3b4660;
  --accent:#d4862f;
}
*{box-sizing:border-box;margin:0;padding:0}
html,body{width:1200px;height:1121px;overflow:hidden}
body{position:relative;background:var(--page);font-family:'Roboto',sans-serif;color:var(--text-nav)}
.sidebar{position:absolute;left:0;top:0;width:244px;height:1058px;background:#fff;border-right:1px solid #cfd2d6}
.brand{position:absolute;left:0;top:40px;width:244px;text-align:center}
.brand-mark{display:inline-block;width:14px;height:14px;border-radius:50%;background:var(--navy);vertical-align:middle;margin-right:6px}
.brand-name{font-size:17px;font-weight:500;color:var(--navy);vertical-align:middle}
.nav{position:absolute;left:0;top:152px;width:244px;list-style:none}
.nav li{height:35.6px;border-bottom:1px solid #c9ccd2;display:flex;align-items:center;padding-left:48px;font-size:13.6px;color:var(--text-nav)}
.nav svg{width:18px;height:18px;margin-right:12px;fill:var(--icon)}
.topbar{position:absolute;left:244px;top:0;width:956px;height:104px;background:linear-gradient(180deg,#27416b,#1a2c4d)}
.search{position:absolute;left:89px;top:31px;width:369px;height:38px;border:1px solid #aab4c6;display:flex;align-items:center;padding-left:12px;color:#d8dfea;font-size:12.5px;letter-spacing:.3px}
.search svg{width:16px;height:16px;margin-right:9px}
.top-icon{position:absolute;top:36px;width:24px;height:24px;fill:#8291ab}
.divider{position:absolute;top:0;width:1px;height:104px;background:#3e557c}
.user{position:absolute;left:727px;top:30px;display:flex;align-items:center}
.avatar-top{width:42px;height:42px;border-radius:50%;background:linear-gradient(135deg,#c9b3a0,#6b5848)}
.user-text{margin-left:9px;color:#e7ecf3;font-size:12.5px;line-height:18px;font-weight:300}
.user-text strong{font-weight:400;font-size:13px;display:block}
.page-title{position:absolute;left:280px;top:152px;font-size:22.4px;font-weight:400;color:var(--navy-dark)}
.sort{position:absolute;left:879px;top:150px;display:flex;align-items:center;font-size:13.6px;color:#2c3650}
.select{margin-left:14px;width:135px;height:29px;background:#fff;border:1px solid #c6c9ce;display:flex;align-items:center;justify-content:space-between;padding:0 10px;font-size:12.5px;color:#475066}
.list{position:absolute;left:280px;top:205px;width:794px;display:flex;flex-direction:column;gap:4px}
.question{position:relative;height:104px;background:var(--card);border:1px solid var(--line)}
.q-photo{position:absolute;left:23px;top:20px;width:52px;height:52px;border-radius:50%;background:linear-gradient(135deg,#b49d8a,#4f4437)}
.q-title{position:absolute;left:83px;top:26px;font-size:13.6px;font-weight:500;color:var(--navy)}
.q-meta{position:absolute;left:85px;top:50px;font-size:11.2px;color:var(--meta);width:640px}
.q-meta span{position:absolute;white-space:nowrap;display:flex;align-items:center}
.q-meta em{font-style:normal;color:var(--accent);margin-left:3px}
.q-meta svg{width:14px;height:14px;margin-right:3px}
.badge{position:absolute;left:698px;top:16px;width:68px;height:68px;border-radius:50%;color:#fff;text-align:center;display:flex;flex-direction:column;justify-content:center;line-height:1}
.badge b{font-weight:400;font-size:25px}
.badge small{font-size:11.5px;margin-top:2px}
.badge.answered{background:var(--badge-navy)}
.badge.open{background:var(--gold)}
.more{position:absolute;left:656px;top:975px;width:28px;height:18px}
.footer{position:absolute;left:0;top:1058px;width:1200px;height:63px;background:var(--footer);color:#f6e7d3;font-size:12px;font-weight:300}
.footer p{position:absolute;left:0;width:1144px;top:23px;text-align:center}
.page-code{position:absolute;right:29px;bottom:4px;color:#fff;font-size:11.5px}
</style>
</head>
<body>
<aside class="sidebar">
  <div class="brand"><span class="brand-mark"></span><span class="brand-name">Harcombe Learning</span></div>
  <ul class="nav">
    <li><svg viewBox="0 0 20 20"><path d="M10 3a8 8 0 0 0-8 8v4h16v-4a8 8 0 0 0-8-8zm1 9H9l1-5z"/></svg>Dashboard</li>
    <li><svg viewBox="0 0 20 20"><path d="M2 4h3v2H2zm5 0h11v2H7zM2 9h3v2H2zm5 0h11v2H7zm-5 5h3v2H2zm5 0h11v2H7z"/></svg>Category Manager</li>
    <li><svg viewBox="0 0 20 20"><circle cx="10" cy="6" r="4"/><path d="M2 18c0-5 4-7 8-7s8 2 8 7z"/></svg>User Manager</li>
    <li><svg viewBox="0 0 20 20"><path d="M4 1h8l5 5v13H4zm8 0v5h5"/></svg>File Manager</li>
    <li><svg viewBox="0 0 20 20"><circle cx="10" cy="10" r="9" fill="none" stroke="#7182a6" stroke-width="1.6"/><circle cx="10" cy="10" r="5.5" fill="none" stroke="#7182a6" stroke-width="1.6"/><circle cx="10" cy="10" r="2.5"/></svg>Emoticon Manager</li>
    <li><svg viewBox="0 0 20 20"><path d="M1 2h1.5v15H19v1.5H1z"/><path d="M4 14l4-5 3 3 6-7" fill="none" stroke="#7182a6" stroke-width="1.6"/></svg>Rank Manager</li>
    <li><svg viewBox="0 0 20 20"><path d="M1 3h18v12H1zm1.6 1.6v8.8h14.8V4.6zM7 16h6v2H7z"/></svg>Template Manager</li>
    <li><svg viewBox="0 0 20 20"><circle cx="10" cy="10" r="9"/><path d="M5.5 10l3 3 6-6" fill="none" stroke="#fff" stroke-width="2"/></svg>Configuration</li>
    <li><svg viewBox="0 0 20 20"><path d="M8 1h4v4H8zM9.3 5h1.4v3H17v4h-1.4V9.4H10.7V12H9.3V9.4H4.4V12H3V8h6.3zM1 12h5v6H1zm6.5 0h5v6h-5zm6.5 0h5v6h-5z"/></svg>Plug-in Manager</li>
    <li><svg viewBox="0 0 20 20"><path d="M13 1a5 5 0 0 0-4.6 7L1 15.4 3.6 18 11 10.6A5 5 0 0 0 18 6l-3 1-2-2 1-3z"/></svg>Forum Tools</li>
    <li><svg viewBox="0 0 20 20"><path d="M3 3h14v2H3zM7 1h6v2H7zM4 6h12l-1 13H5zm3 2v9h1.4V8zm4.6 0v9H13V8z"/></svg>Trash Manager</li>
  </ul>
</aside>

<header class="topbar">
  <div class="search"><svg viewBox="0 0 20 20"><circle cx="8" cy="8" r="6" fill="none" stroke="#fff" stroke-width="2.5"/><path d="M12.5 12.5l6 6" stroke="#fff" stroke-width="3"/></svg>SEARCH HERE</div>
  <svg class="top-icon" style="left:546px" viewBox="0 0 24 24"><path d="M12 2a2 2 0 0 1 2 2v.5A7 7 0 0 1 19 11v5l2 2v1H3v-1l2-2v-5a7 7 0 0 1 5-6.5V4a2 2 0 0 1 2-2zm-2 18h4a2 2 0 0 1-4 0z"/></svg>
  <div class="divider" style="left:611px"></div>
  <svg class="top-icon" style="left:640px" viewBox="0 0 24 24"><path d="M10 1h4l.6 3 2.5 1.1 2.6-1.7 2.8 2.8-1.7 2.6L22 11v2l-3 .6-1.1 2.6 1.7 2.6-2.8 2.8-2.6-1.7-2.2.9L14 23h-4l-.6-3-2.5-1-2.6 1.7-2.8-2.8 1.7-2.6L2 13v-2l3-.6 1.1-2.5-1.7-2.6 2.8-2.8 2.6 1.7L10 4zm2 7a4 4 0 1 0 0 8 4 4 0 0 0 0-8z"/></svg>
  <div class="divider" style="left:694px"></div>
  <div class="user"><div class="avatar-top" role="img" aria-label="Signed-in user photo"></div><div class="user-text">Welcome<strong>Daniel Mercer</strong></div></div>
</header>

<h1 class="page-title">Recent Forum Questions</h1>
<div class="sort">Sort by<div class="select">Ascending<svg width="12" height="8" viewBox="0 0 12 8"><path d="M1 1l5 5 5-5" fill="none" stroke="#556" stroke-width="1.4"/></svg></div></div>

<main class="list">
  <article class="question"><div class="q-photo" role="img" aria-label="Member photo"></div><h2 class="q-title">Praesent elementum elit at tellus nec ultricies sit amet porttitor</h2><div class="q-meta"><span style="left:0">Updated 5 minutes ago</span><span style="left:134px">Asked by<em>Lena Hartfield</em></span><span style="left:292px;top:1px">Last reply by<em>Marcus</em></span><span style="left:413px;top:-1px"><svg viewBox="0 0 16 16"><path fill="#d4862f" d="M8 2c4 0 7 2.2 7 5s-3 5-7 5l-5 2 1.5-3A5 5 0 0 1 1 7c0-2.8 3-5 7-5z"/></svg>25</span><span style="left:464px;top:-1px"><svg viewBox="0 0 16 16"><path fill="none" stroke="#d4862f" stroke-width="1.7" d="M8 14L2.3 8.3A3.3 3.3 0 0 1 8 4a3.3 3.3 0 0 1 5.7 4.3z"/></svg>17</span></div><div class="badge answered"><b>1</b><small>Answer</small></div></article>
  <article class="question"><div class="q-photo" role="img" aria-label="Member photo"></div><h2 class="q-title">Aermentum vel congue id euismod in elit</h2><div class="q-meta"><span style="left:0">Updated 5 minutes ago</span><span style="left:134px">Asked by<em>Lena Hartfield</em></span><span style="left:292px;top:1px">Last reply by<em>Marcus</em></span><span style="left:413px;top:-1px"><svg viewBox="0 0 16 16"><path fill="#d4862f" d="M8 2c4 0 7 2.2 7 5s-3 5-7 5l-5 2 1.5-3A5 5 0 0 1 1 7c0-2.8 3-5 7-5z"/></svg>25</span><span style="left:464px;top:-1px"><svg viewBox="0 0 16 16"><path fill="none" stroke="#d4862f" stroke-width="1.7" d="M8 14L2.3 8.3A3.3 3.3 0 0 1 8 4a3.3 3.3 0 0 1 5.7 4.3z"/></svg>17</span></div><div class="badge answered"><b>1</b><small>Answer</small></div></article>
  <article class="question"><div class="q-photo" role="img" aria-label="Member photo"></div><h2 class="q-title">Praesent elementum elit at tellus nec ultricies sit amet porttitor</h2><div class="q-meta"><span style="left:0">Updated 5 minutes ago</span><span style="left:134px">Asked by<em>Lena Hartfield</em></span><span style="left:292px;top:1px">Last reply by<em>Marcus</em></span><span style="left:413px;top:-1px"><svg viewBox="0 0 16 16"><path fill="#d4862f" d="M8 2c4 0 7 2.2 7 5s-3 5-7 5l-5 2 1.5-3A5 5 0 0 1 1 7c0-2.8 3-5 7-5z"/></svg>25</span><span style="left:464px;top:-1px"><svg viewBox="0 0 16 16"><path fill="none" stroke="#d4862f" stroke-width="1.7" d="M8 14L2.3 8.3A3.3 3.3 0 0 1 8 4a3.3 3.3 0 0 1 5.7 4.3z"/></svg>17</span></div><div class="badge answered"><b>1</b><small>Answer</small></div></article>
  <article class="question"><div class="q-photo" role="img" aria-label="Member photo"></div><h2 class="q-title">Mauris vel lacus vitae felis vestibulum volutpat Etiam</h2><div class="q-meta"><span style="left:0">Updated 5 minutes ago</span><span style="left:134px">Asked by<em>Lena Hartfield</em></span><span style="left:292px;top:1px">Last reply by<em>Marcus</em></span><span style="left:413px;top:-1px"><svg viewBox="0 0 16 16"><path fill="#d4862f" d="M8 2c4 0 7 2.2 7 5s-3 5-7 5l-5 2 1.5-3A5 5 0 0 1 1 7c0-2.8 3-5 7-5z"/></svg>25</span><span style="left:464px;top:-1px"><svg viewBox="0 0 16 16"><path fill="none" stroke="#d4862f" stroke-width="1.7" d="M8 14L2.3 8.3A3.3 3.3 0 0 1 8 4a3.3 3.3 0 0 1 5.7 4.3z"/></svg>17</span></div><div class="badge open"><b>NO</b><small>Answer</small></div></article>
  <article class="question"><div class="q-photo" role="img" aria-label="Member photo"></div><h2 class="q-title">Lorem ipsum dolor sit amet consectetuer adipiscing</h2><div class="q-meta"><span style="left:0">Updated 5 minutes ago</span><span style="left:134px">Asked by<em>Lena Hartfield</em></span><span style="left:292px;top:1px">Last reply by<em>Marcus</em></span><span style="left:413px;top:-1px"><svg viewBox="0 0 16 16"><path fill="#d4862f" d="M8 2c4 0 7 2.2 7 5s-3 5-7 5l-5 2 1.5-3A5 5 0 0 1 1 7c0-2.8 3-5 7-5z"/></svg>25</span><span style="left:464px;top:-1px"><svg viewBox="0 0 16 16"><path fill="none" stroke="#d4862f" stroke-width="1.7" d="M8 14L2.3 8.3A3.3 3.3 0 0 1 8 4a3.3 3.3 0 0 1 5.7 4.3z"/></svg>17</span></div><div class="badge answered"><b>1</b><small>Answer</small></div></article>
  <article class="question"><div class="q-photo" role="img" aria-label="Member photo"></div><h2 class="q-title">Praesent elementum elit at tellus nec ultricies sit amet porttitor</h2><div class="q-meta"><span style="left:0">Updated 5 minutes ago</span><span style="left:134px">Asked by<em>Lena Hartfield</em></span><span style="left:292px;top:1px">Last reply by<em>Marcus</em></span><span style="left:413px;top:-1px"><svg viewBox="0 0 16 16"><path fill="#d4862f" d="M8 2c4 0 7 2.2 7 5s-3 5-7 5l-5 2 1.5-3A5 5 0 0 1 1 7c0-2.8 3-5 7-5z"/></svg>25</span><span style="left:464px;top:-1px"><svg viewBox="0 0 16 16"><path fill="none" stroke="#d4862f" stroke-width="1.7" d="M8 14L2.3 8.3A3.3 3.3 0 0 1 8 4a3.3 3.3 0 0 1 5.7 4.3z"/></svg>17</span></div><div class="badge answered"><b>1</b><small>Answer</small></div></article>
  <article class="question"><div class="q-photo" role="img" aria-label="Member photo"></div><h2 class="q-title">Quisque dignissim congue leo</h2><div class="q-meta"><span style="left:0">Updated 5 minutes ago</span><span style="left:134px">Asked by<em>Lena Hartfield</em></span><span style="left:292px;top:1px">Last reply by<em>Marcus</em></span><span style="left:413px;top:-1px"><svg viewBox="0 0 16 16"><path fill="#d4862f" d="M8 2c4 0 7 2.2 7 5s-3 5-7 5l-5 2 1.5-3A5 5 0 0 1 1 7c0-2.8 3-5 7-5z"/></svg>25</span><span style="left:464px;top:-1px"><svg viewBox="0 0 16 16"><path fill="none" stroke="#d4862f" stroke-width="1.7" d="M8 14L2.3 8.3A3.3 3.3 0 0 1 8 4a3.3 3.3 0 0 1 5.7 4.3z"/></svg>17</span></div><div class="badge open"><b>NO</b><small>Answer</small></div></article>
</main>

<svg class="more" viewBox="0 0 28 18"><path d="M2 3l12 12L26 3" fill="none" stroke="#8a8f98" stroke-width="3"/></svg>

<footer class="footer"><p>© 2018 Company Name &nbsp;All right reserved &nbsp;Terms of Use</p><span class="page-code">X14</span></footer>
</body>
</html>
```